Brookvale Systems Yellow rose letterhead

I have a new logo for my company but in its current form it is too large to be used on letterhead or as a email signature. I need to have the designer use elements from the current logo and create something close to the original but more suited for smaller items.
Updates

I just uploaded a copy of our logo that does not have the weathered affect. Thanks

Industry/Entity Type

It Company

Requirements
Must have
• The design must maintain the visual effect of the current logo. It needs to include the yellow rose and the name of the company.
Nice to have
• It would be nice to maintain the stamp theme and incorporate my name, address, phone, email. etc.

```html
<!DOCTYPE html>
<html lang="en">
<head>
<meta charset="utf-8">
<title>Brookvale Systems Letterhead</title>
<link href="https://fonts.googleapis.com/css2?family=Baloo+2:wght@500&display=swap" rel="stylesheet">
<style>
  :root {
    --sun-yellow: #fdc31a;
    --pale-yellow: #fde8a3;
    --cream: #fffaf0;
    --paper: #ffffff;
    --teal: #3ab9c3;
    --stamp-brown: #4a3f38;
  }
  html, body {
    margin: 0;
    padding: 0;
    overflow: hidden;
    background: var(--paper);
  }
  .letterhead {
    position: relative;
    width: 930px;
    height: 1200px;
    overflow: hidden;
    background: var(--paper);
    font-family: "Baloo 2", "Trebuchet MS", sans-serif;
  }
  .letterhead__art {
    position: absolute;
    inset: 0;
    width: 930px;
    height: 1200px;
  }
  .brand {
    position: absolute;
    top: 92px;
    right: 44px;
    display: flex;
    align-items: center;
    gap: 12px;
    color: var(--teal);
    font-weight: 500;
    font-size: 32px;
    line-height: 1;
  }
  .brand__mark {
    width: 26px;
    height: 26px;
    background: var(--stamp-brown);
  }
  .contact {
    position: absolute;
    left: 21px;
    top: 520px;
    margin: 0;
    font-style: normal;
    color: var(--teal);
    font-weight: 500;
    font-size: 15px;
    line-height: 27px;
  }
  .contact span { display: block; }
</style>
</head>
<body>
<div class="letterhead">
  <svg class="letterhead__art" viewBox="0 0 930 1200" aria-hidden="true">
    <defs>
      <linearGradient id="header-fade" x1="0" y1="0" x2="0" y2="1">
        <stop offset="0" stop-color="#fdd25a"/>
        <stop offset="0.45" stop-color="#fdeebb"/>
        <stop offset="1" stop-color="#ffffff"/>
      </linearGradient>
      <radialGradient id="header-glow" cx="0.38" cy="0.08" r="0.55">
        <stop offset="0" stop-color="#fffdf4"/>
        <stop offset="0.55" stop-color="#fde59a"/>
        <stop offset="1" stop-color="#fdc31a"/>
      </radialGradient>
      <radialGradient id="footer-glow" cx="0.45" cy="0.7" r="0.6">
        <stop offset="0" stop-color="#ffffff"/>
        <stop offset="0.45" stop-color="#fde9a8"/>
        <stop offset="1" stop-color="#fdc31a"/>
      </radialGradient>
    </defs>
    <rect class="header-wash" x="0" y="0" width="930" height="700" fill="url(#header-fade)"/>
    <path class="header-band" d="M0,0 H930 V228 C880,238 830,258 760,260 C640,262 540,170 420,162 C300,152 150,185 0,240 Z" fill="url(#header-glow)"/>
    <path class="header-wave" d="M0,240 C150,185 300,152 420,162 C540,170 640,262 760,260 C830,258 880,238 930,228" fill="none" stroke="var(--teal)" stroke-width="12"/>
    <path class="footer-band" d="M0,1072 C200,1038 400,1030 560,1056 C700,1080 820,1128 930,1118 V1200 H0 Z" fill="url(#footer-glow)"/>
  </svg>

  <div class="brand">
    <span class="brand__mark"></span>
    <span class="brand__name">Brookvale Systems</span>
  </div>

  <address class="contact">
    <span>Mara Ellison, PhD</span>
    <span>418 NE Cedar Ridge Trail, Ste 2107</span>
    <span>Millbrook, TX 76511</span>
    <span>mara@brookvale-systems.com</span>
    <span>1-800-555-0147</span>
  </address>
</div>
</body>
</html>
```